Supplement Rebranding Bottle Design

READ WORD DOCUMENT ATTACHED.
We want to rebrand our current health supplements (see below). We do want it to be modern, vibrant and appealing. Very upscale and elegant as it targets primarily women.
Bottle size: see pictures for bottle size, along with sample bottles that we like; we’re open to any bottle similar to the ones attached.
Current bottles: So ideally, we’d keep the core color on each bottle with a new branding/bottle design. But we're open to your suggestion.

Target Market(s)

mostly women but shouldn't be overly feminine

Requirements
Must have
• see bottle sizes attached

```html
<!DOCTYPE html>
<html lang="en">
<head>
<meta charset="utf-8">
<title>Lumera Balance – Label</title>
<link rel="stylesheet" href="https://fonts.googleapis.com/css2?family=Lexend:wght@300;400;800&display=swap">
<style>
  :root {
    --page: #ffffff;
    --lime: #d8f150;
    --lime-soft: #eefaa6;
    --lime-glow: #f6fdd2;
    --forest: #0f5a16;
    --rule: #2f7a1c;
    --helix: #8cc63a;
  }
  * { margin: 0; padding: 0; box-sizing: border-box; }
  html, body {
    width: 797px;
    height: 1200px;
    overflow: hidden;
    background: var(--page);
    font-family: "Lexend", sans-serif;
  }
  .label {
    position: absolute;
    left: 33px;
    top: 310px;
    width: 730px;
    height: 580px;
    overflow: hidden;
    background:
      radial-gradient(ellipse 60% 45% at 22% 18%, var(--lime-glow) 0%, rgba(246,253,210,0) 70%),
      radial-gradient(ellipse 55% 40% at 95% 78%, var(--lime-glow) 0%, rgba(246,253,210,0) 70%),
      linear-gradient(160deg, var(--lime-soft) 0%, var(--lime) 45%, var(--lime-soft) 100%);
  }
  .helix-art {
    position: absolute;
    left: 162px;
    top: 91px;
    width: 224px;
    height: 206px;
    border-radius: 40px;
    background: radial-gradient(ellipse at center, rgba(140,198,58,0.35) 0%, rgba(140,198,58,0) 70%);
  }
  .lead-line {
    position: absolute;
    left: 0;
    top: 273px;
    width: 218px;
    height: 2px;
    background: var(--helix);
  }
  .claims {
    position: absolute;
    left: 444px;
    top: 86px;
    width: 204px;
    text-align: right;
    color: var(--forest);
  }
  .claims__tagline {
    font-size: 20px;
    font-weight: 400;
    line-height: 25px;
    letter-spacing: -1.4px;
    text-transform: uppercase;
    padding-bottom: 14px;
    border-bottom: 1.5px solid var(--rule);
  }
  .claims__type {
    font-size: 19px;
    font-weight: 300;
    letter-spacing: -0.6px;
    line-height: 38px;
    border-bottom: 1.5px solid var(--rule);
  }
  .claims__count {
    margin-top: 8px;
    font-size: 20px;
    font-weight: 300;
    line-height: 22px;
  }
  .claims__form {
    font-size: 14px;
    font-weight: 300;
    line-height: 18px;
    letter-spacing: -0.3px;
  }
  .product-name {
    position: absolute;
    left: 168px;
    top: 330px;
    font-size: 84px;
    font-weight: 800;
    line-height: 88px;
    letter-spacing: -4px;
    color: var(--forest);
  }
  .product-name span { display: block; }
</style>
</head>
<body>
  <section class="label">
    <div class="helix-art" role="img" aria-label="Line illustration of a DNA double helix"></div>
    <div class="lead-line"></div>

    <div class="claims">
      <p class="claims__tagline">Supports healthy hormone levels</p>
      <p class="claims__type">Dietary Supplement</p>
      <p class="claims__count">60</p>
      <p class="claims__form">Vegetable Capsules</p>
    </div>

    <h1 class="product-name">
      <span>Lumera</span>
      <span>Balance</span>
    </h1>
  </section>
</body>
</html>
```